Web Design Project

We need a web site that reflects our young vibratant company. We are a heating and airconditioning company that provides installations using the latest and most energy efficient products.

Our company is technology based and we like a fresh style like the quorvix.com web site or the brelta.com web site
Updates

this is a guaranteed payment project

Target Market(s)

mums and dads and architects

Industry/Entity Type

It Company

Requirements
Must have
• we want the web site to have the ability to upload files for customers to upload house plans and photos.

```html
<!DOCTYPE html>
<html lang="en">
<head>
<meta charset="utf-8">
<title>Thermora — Smart Heating &amp; Cooling</title>
<link rel="stylesheet" href="https://fonts.googleapis.com/css2?family=Noto+Sans:ital,wght@0,400;0,700;1,400;1,700&family=Noto+Serif:ital@1&display=swap">
<style>
  :root {
    --page: #f4f4f2;
    --ink: #222222;
    --muted: #7a7a7a;
    --orange: #f07d1a;
    --headline: #f05a14;
    --blue: #2a9ad0;
    --sky: #45b6e8;
    --line: #d6d6d6;
    --card: #f7f7f7;
    --field: #e6e6e6;
    --go-blue: #2a93c4;
    --go-gold: #dba858;
    --icon: #b9b9b9;
  }
  * { box-sizing: border-box; margin: 0; padding: 0; }
  html, body { width: 1200px; height: 819px; overflow: hidden; }
  body {
    position: relative;
    background: var(--page);
    font-family: "Noto Sans", Tahoma, sans-serif;
    color: var(--ink);
  }
  .brand {
    position: absolute; left: 140px; top: 80px;
    display: flex; align-items: center; gap: 10px;
    font-size: 30px; line-height: 38px; color: var(--orange); text-decoration: none;
  }
  .brand-dot { width: 26px; height: 26px; border-radius: 50%; background: var(--sky); }
  .search { position: absolute; left: 853px; top: 41px; display: flex; gap: 7px; }
  .search-field { width: 201px; height: 28px; border: none; border-radius: 3px; background: var(--field); }
  .search-go {
    width: 39px; height: 27px; border: none; border-radius: 2px;
    background: linear-gradient(#4cb3df, var(--go-blue)); color: #fff; font: 13px "Noto Sans", sans-serif;
  }
  .main-nav a {
    position: absolute; top: 96px; font-size: 15px; color: var(--orange); text-decoration: none;
  }
  .main-nav a.current { color: var(--blue); }
  .hero {
    position: absolute; left: 0; top: 140px; width: 1200px; height: 334px;
    border-top: 1px solid var(--line); border-bottom: 1px solid var(--line);
    background: linear-gradient(90deg, #ecebe4 0%, #e3e4e6 40%, #ecece6 70%, #f1f1ec 100%);
    overflow: hidden;
  }
  .hero-backdrop {
    position: absolute; left: 275px; top: -40px; width: 510px; height: 420px;
    background: radial-gradient(ellipse at center, #d8dbe3 0%, #dde0e6 50%, rgba(230,230,226,0) 75%);
  }
  .hero-title {
    position: absolute; left: 246px; top: 259px;
    font-family: "Noto Serif", Georgia, serif; font-style: italic; font-weight: 400;
    font-size: 39px; line-height: 46px; color: var(--headline); letter-spacing: 0.6px;
  }
  .hero-more {
    position: absolute; left: 505px; top: 363px;
    font-style: italic; font-size: 14px; color: var(--sky); text-decoration: none;
    display: flex; align-items: center; gap: 6px;
  }
  .hero-more::before {
    content: ""; width: 0; height: 0;
    border-left: 12px solid var(--blue); border-top: 8px solid transparent; border-bottom: 8px solid transparent;
  }
  .device-placeholder {
    position: absolute; left: 823px; top: 169px; width: 276px; height: 274px;
    background: linear-gradient(160deg, #8e93a8 0%, #3a3f66 50%, #3c4fc8 100%);
  }
  .card {
    position: absolute; top: 495px; width: 280px; height: 193px;
    background: var(--card); border: 1px solid #e0e0e0; border-radius: 3px;
    box-shadow: 0 1px 3px rgba(0,0,0,0.15);
  }
  .card-video { left: 91px; }
  .card-upload { left: 458px; }
  .card-news { left: 826px; }
  .video-still {
    position: absolute; left: 16px; top: 14px; width: 250px; height: 168px;
    background: linear-gradient(135deg, #c6ccd4 0%, #e7e2dc 55%, #d8c8b6 100%);
  }
  .play-btn {
    position: absolute; left: 46px; top: 73px; width: 180px; height: 51px; border-radius: 3px;
    background: rgba(70,70,70,0.75); color: #fff; font-weight: 700; font-style: italic; font-size: 17px;
    display: flex; align-items: center; gap: 22px; padding-left: 14px;
  }
  .play-btn svg { flex: none; }
  .upload-icon { position: absolute; left: 18px; top: 18px; }
  .upload-title { position: absolute; left: 153px; top: 32px; font-weight: 700; font-style: italic; font-size: 17px; }
  .upload-text { position: absolute; left: 153px; top: 61px; width: 120px; font-size: 11.5px; line-height: 14px; }
  .upload-form { position: absolute; left: 32px; top: 145px; display: flex; gap: 5px; }
  .upload-field { width: 185px; height: 34px; border: 1px solid #cfcfcf; border-radius: 3px; background: var(--field); }
  .upload-go {
    width: 44px; height: 32px; border: none; border-radius: 2px;
    background: linear-gradient(#e8bf72, var(--go-gold)); color: #fff; font: 12px "Noto Sans", sans-serif;
  }
  .news-title { position: absolute; left: 33px; top: 29px; font-style: italic; font-weight: 400; font-size: 15px; }
  .news-visual {
    position: absolute; left: 45px; top: 70px; width: 180px; height: 100px;
    background: linear-gradient(120deg, #2b2b2b 0%, #3b4a5e 45%, #7fb8e8 60%, #e9eef2 100%);
  }
  .news-more {
    position: absolute; left: 10px; top: 162px; width: 76px; height: 23px; border-radius: 2px;
    background: linear-gradient(#cfcfcf, #a9a9a9); color: #333; font-size: 11px; font-style: italic;
    text-decoration: none; display: flex; align-items: center; justify-content: center;
  }
  .footer {
    position: absolute; left: 83px; top: 726px; width: 1027px; height: 58px;
    border-top: 1px solid var(--line); border-bottom: 1px solid var(--line);
    font-size: 12px; color: var(--muted);
  }
  .footer a, .footer span { position: absolute; top: 24px; color: var(--muted); text-decoration: none; }
  .footer a.highlight { color: #e8441c; }
  .footer .social { top: 14px; width: 31px; height: 31px; border-radius: 4px; background: linear-gradient(#d6d6d6, var(--icon)); }
  .footer .social.dark { background: linear-gradient(#444, #1e1e1e); }
</style>
</head>
<body>
  <header>
    <a class="brand" href="#"><span class="brand-dot"></span>Thermora</a>
    <form class="search"><input class="search-field" type="text" aria-label="Search"><button class="search-go" type="button">Go</button></form>
    <nav class="main-nav">
      <a href="#" style="left:582px">Our thermostat</a>
      <a href="#" class="current" style="left:742px">About us</a>
      <a href="#" style="left:858px">Blog</a>
      <a href="#" style="left:936px">Support</a>
      <a href="#" style="left:1040px">Preorder</a>
    </nav>
  </header>

  <section class="hero">
    <div class="hero-backdrop" role="img" aria-label="Faint enlarged thermostat display in the background"></div>
  </section>
  <h1 class="hero-title">Programe&nbsp; itself so you<br>don't have to.</h1>
  <a class="hero-more" href="#">Read More</a>
  <div class="device-placeholder" role="img" aria-label="Product photo of the round smart thermostat showing 72 degrees"></div>

  <main>
    <article class="card card-video">
      <div class="video-still" role="img" aria-label="Hand holding a phone with the climate control app"></div>
      <div class="play-btn">
        <svg width="26" height="26" viewBox="0 0 26 26"><circle cx="13" cy="13" r="11" fill="none" stroke="#fff" stroke-width="2"/><path d="M10 7l7 6-7 6" fill="none" stroke="#fff" stroke-width="2"/></svg>
        Play Video
      </div>
    </article>

    <article class="card card-upload">
      <svg class="upload-icon" width="116" height="116" viewBox="0 0 116 116">
        <defs><radialGradient id="orb" cx="0.45" cy="0.35" r="0.7"><stop offset="0" stop-color="#ffb43a"/><stop offset="1" stop-color="#f06a00"/></radialGradient></defs>
        <circle cx="58" cy="58" r="57" fill="#e6e6e6" stroke="#cfcfcf"/>
        <circle cx="58" cy="58" r="49" fill="url(#orb)"/>
        <path d="M58 22 L86 52 L70 52 L70 90 L46 90 L46 52 L30 52 Z" fill="#fff"/>
      </svg>
      <h2 class="upload-title">upload</h2>
      <p class="upload-text">Dolor sit amet, consectetur adipisic-ing consectetur adipisicing</p>
      <form class="upload-form"><input class="upload-field" type="text" aria-label="File to upload"><button class="upload-go" type="button">Go</button></form>
    </article>

    <article class="card card-news">
      <h2 class="news-title">What’s new</h2>
      <div class="news-visual" role="img" aria-label="Two touch-screen climate control panels"></div>
      <a class="news-more" href="#">Read More</a>
    </article>
  </main>

  <footer class="footer">
    <a href="#" style="left:5px">Responsibility</a>
    <a href="#" class="highlight" style="left:126px">Careers</a>
    <a href="#" style="left:220px">Press</a>
    <a href="#" style="left:297px">Brelta Certified</a>
    <span style="left:455px">© 2012 Thermora</span>
    <a href="#" style="left:576px">Terms and privacy</a>
    <span class="social dark" style="left:810px" aria-label="Social link"></span>
    <span class="social" style="left:855px" aria-label="Social link"></span>
    <span class="social" style="left:900px" aria-label="Social link"></span>
    <span class="social" style="left:945px" aria-label="Social link"></span>
    <span class="social" style="left:990px" aria-label="Social link"></span>
  </footer>
</body>
</html>
```